Packaging Design Project

We need a packaging design for a portable solar charger and 3-way cable.
The package style that is added in the pictures is preferred but we are open to suggestions.
I also added the cut line for the paper with fold lines

Industry/Entity Type

Solar

```html
<!DOCTYPE html>
<html lang="en">
<head>
<meta charset="utf-8">
<title>Solar Charger Box Dieline</title>
<link rel="stylesheet" href="https://fonts.googleapis.com/css2?family=Quicksand:wght@400;500;700&family=Arimo&display=swap">
<style>
  :root {
    --paper: #ffffff;
    --teal: #1b8ba5;
    --flap: #93e9f6;
    --ink-dark: #0e4553;
    --cream: #f6efb4;
    --line-white: #ffffff;
    --hanger-red: #c0394a;
  }
  html, body {
    margin: 0;
    padding: 0;
    width: 1200px;
    height: 768px;
    overflow: hidden;
    background: var(--paper);
  }
  .dieline { display: block; width: 1200px; height: 768px; }
  .panel { fill: var(--teal); }
  .flap { fill: var(--flap); }
  .rule { stroke: var(--line-white); stroke-width: 2.2; }
  .brand-word {
    font-family: "Quicksand", sans-serif;
    font-weight: 400;
    fill: var(--ink-dark);
  }
  .product-name {
    font-family: "Quicksand", sans-serif;
    font-weight: 700;
    fill: var(--cream);
    letter-spacing: 0.5px;
  }
  .info-heading {
    font-family: "Arimo", sans-serif;
    font-size: 8px;
    fill: var(--line-white);
  }
  .window { fill: #ffffff; stroke: var(--cream); stroke-width: 5; }
</style>
</head>
<body>
<svg class="dieline" viewBox="0 0 1052 680" preserveAspectRatio="xMidYMid meet" xmlns="http://www.w3.org/2000/svg">
  <defs>
    <filter id="window-glow" x="-30%" y="-30%" width="160%" height="160%">
      <feGaussianBlur stdDeviation="5"/>
    </filter>
    <linearGradient id="skyline-tone" x1="0" y1="0" x2="0" y2="1">
      <stop offset="0" stop-color="#8fd3e0" stop-opacity="0.75"/>
      <stop offset="1" stop-color="#8fd3e0" stop-opacity="0.35"/>
    </linearGradient>
  </defs>

  <!-- hang tab flap above back panel -->
  <rect class="flap" x="73" y="25" width="244" height="153"/>
  <path d="M121 74 Q185 58 250 74 L246 79 Q185 68 125 79 Z" fill="#ffffff" stroke="var(--hanger-red)" stroke-width="0.8"/>
  <path d="M186 64 Q190 56 194 64" fill="#ffffff" stroke="var(--hanger-red)" stroke-width="0.8"/>
  <g class="flap-rules">
    <line class="rule" x1="87" y1="133" x2="208" y2="133"/>
    <line class="rule" x1="87" y1="138" x2="196" y2="138"/>
    <line class="rule" x1="87" y1="143" x2="184" y2="143"/>
    <line class="rule" x1="87" y1="149" x2="196" y2="149"/>
  </g>

  <!-- front panel tuck flaps -->
  <polygon class="flap" points="377,157 596,157 608,178 365,178"/>
  <polygon class="flap" points="365,632 608,632 596,652 377,652"/>

  <!-- glue flap -->
  <polygon class="panel" points="30,178 73,178 73,632 30,632 24,596 24,214"/>
  <!-- back panel -->
  <rect class="panel" x="73" y="178" width="244" height="454"/>
  <!-- left spine with dust flaps -->
  <polygon class="panel" points="322,178 365,178 365,632 322,632 317,596 317,214"/>
  <!-- front panel -->
  <rect class="panel" x="365" y="178" width="243" height="454"/>
  <!-- right spine with dust flaps -->
  <polygon class="panel" points="608,178 650,178 655,214 655,596 650,632 608,632"/>
  <!-- closing panel -->
  <polygon class="panel" points="740,178 960,178 960,228 1032,228 1032,582 960,582 960,632 740,632 740,582 655,582 655,228 740,228"/>

  <!-- back panel copy -->
  <g class="back-copy">
    <text class="info-heading" x="87" y="247">Features</text>
    <line class="rule" x1="87" y1="255" x2="162" y2="255"/>
    <line class="rule" x1="87" y1="262" x2="150" y2="262"/>
    <line class="rule" x1="87" y1="270" x2="168" y2="270"/>
    <line class="rule" x1="87" y1="277" x2="160" y2="277"/>
    <line class="rule" x1="87" y1="285" x2="166" y2="285"/>

    <text class="info-heading" x="87" y="308">How to use this device ?</text>
    <line class="rule" x1="87" y1="315" x2="241" y2="315"/>
    <line class="rule" x1="87" y1="322" x2="241" y2="322"/>
    <line class="rule" x1="87" y1="329" x2="241" y2="329"/>
    <line class="rule" x1="87" y1="336" x2="241" y2="336"/>
    <line class="rule" x1="87" y1="343" x2="241" y2="343"/>
    <line class="rule" x1="87" y1="350" x2="241" y2="350"/>
    <line class="rule" x1="87" y1="357" x2="241" y2="357"/>
    <line class="rule" x1="87" y1="364" x2="241" y2="364"/>

    <text class="info-heading" x="87" y="390">For Complaints</text>
    <line class="rule" x1="87" y1="398" x2="241" y2="398"/>
    <line class="rule" x1="87" y1="405" x2="241" y2="405"/>
    <line class="rule" x1="87" y1="412" x2="241" y2="412"/>
    <line class="rule" x1="87" y1="419" x2="241" y2="419"/>
    <line class="rule" x1="87" y1="426" x2="241" y2="426"/>
    <line class="rule" x1="87" y1="433" x2="241" y2="433"/>
    <line class="rule" x1="87" y1="440" x2="241" y2="440"/>
    <line class="rule" x1="87" y1="447" x2="241" y2="447"/>
    <line class="rule" x1="87" y1="453" x2="241" y2="453"/>

    <text class="info-heading" x="87" y="553">Specifications</text>
    <line class="rule" x1="87" y1="558" x2="209" y2="558"/>
    <line class="rule" x1="87" y1="563" x2="209" y2="563"/>
    <line class="rule" x1="87" y1="568" x2="209" y2="568"/>
    <line class="rule" x1="87" y1="573" x2="155" y2="573"/>

    <text class="info-heading" transform="translate(281 573) rotate(-90)">Mfg. &amp; Batch</text>
    <line class="rule" x1="285" y1="445" x2="285" y2="574"/>
    <line class="rule" x1="290" y1="458" x2="290" y2="574"/>
    <line class="rule" x1="295" y1="463" x2="295" y2="574"/>
    <line class="rule" x1="300" y1="470" x2="300" y2="574"/>
  </g>

  <!-- left spine branding -->
  <g transform="translate(331 320) rotate(90)">
    <text class="brand-word" x="0" y="0" font-size="25">BRAND</text>
    <text class="product-name" x="92" y="-2" font-size="10">SOLAR CHARGER</text>
  </g>

  <!-- front panel branding -->
  <text class="brand-word" x="380" y="216" font-size="27">BRAND</text>
  <text class="product-name" x="478" y="217" font-size="10.5">SOLAR CHARGER</text>
  <text class="brand-word" x="487" y="291" font-size="49" text-anchor="middle" stroke="var(--ink-dark)" stroke-width="0.6">BRAND</text>
  <text class="product-name" x="488" y="309" font-size="16" text-anchor="middle">SOLAR CHARGER</text>

  <rect x="368" y="512" width="239" height="70" fill="url(#skyline-tone)" filter="url(#window-glow)" role="img" aria-label="Soft city skyline silhouette"/>
  <ellipse cx="486" cy="432" rx="84" ry="104" fill="none" stroke="var(--cream)" stroke-width="10" opacity="0.7" filter="url(#window-glow)"/>
  <ellipse class="window" cx="486" cy="432" rx="80" ry="100"/>

  <!-- right spine branding -->
  <g transform="translate(634 516) rotate(-90)">
    <text class="brand-word" x="0" y="0" font-size="25">BRAND</text>
    <text class="product-name" x="92" y="-2" font-size="10">SOLAR CHARGER</text>
  </g>
</svg>
</body>
</html>
```